Stationary for I.T. company
DuskVale
Stationary for I.T. company - Information Technology
Creative Brief
Bright & Fun-filled
Ray Olsen
Director
PO Box 4172 Marlow ACT 2913
ops@duskva.le
duskva.le
Eye catching - display the DuskVale logo with either the red N with the white text or the white only logo on a background with either bold colours, dark greys or black. Open to other concepts or suggestions if they are eye catching
brimlow brimlow
Thank you everyone for your efforts. We may ask a couple more questons to relevant designers - but we plan to decide in the next 24 to 48 hours. Thanks again.
Thanks everyone for your submissions so far.. 266 designs is much much more than we were expecting. To help everyone understand where we are going and what we are looking for we will start eliminating some designs tonight. With that, we will probably start to give out a couple (maybe 3) 5 star ratings. These will indicate the current leading designs. We will probably also redo most of the star ratings out there to better give designers a better understanding of what we like. Please note that there is several people looking at these designs, so star rating may go up and down a little... but be assured if it has stars, we like it, or like some concepts in it.
We will aim to provide every designer feedback and stars (so yes - it may look like we rate a lot of things highly). 4 stars will generally be used to indicate the favorite submission of a designer, and 5 will only be used when we start eliminating designs.
tallfern tallfern
Check your private messages...
Also looking for letter head, invoice, envelope, notepad templates, presentation folder in addition to business card design. Thanks.
Amendment to the design brief - we will also accept a white background for the back of the business card

```html
<!DOCTYPE html>
<html lang="en">
<head>
<meta charset="utf-8">
<title>DuskVale business card</title>
<link rel="stylesheet" href="https://fonts.googleapis.com/css2?family=Open+Sans:wght@400;600;700&display=swap">
<style>
  :root {
    --stage: #8c8c8c;
    --card-dark: #0b0b0b;
    --card-light: #ffffff;
    --brand-red: #d4141c;
    --brand-red-deep: #9e0b10;
    --ink: #3a3a3a;
    --ink-soft: #6a6a6a;
    --on-dark: #d9d9d9;
  }
  * { margin: 0; padding: 0; box-sizing: border-box; }
  html, body { width: 1200px; height: 908px; overflow: hidden; }
  body {
    background: var(--stage);
    font-family: "Open Sans", Arial, sans-serif;
    position: relative;
  }
  .card {
    position: absolute;
    width: 620px;
    height: 354px;
    border-radius: 22px;
    overflow: hidden;
  }
  .card--front {
    left: 110px;
    top: 80px;
    background: var(--card-dark);
    display: flex;
    align-items: center;
    justify-content: center;
  }
  .card--back {
    left: 470px;
    top: 474px;
    background: var(--card-light);
  }
  .wordmark {
    display: flex;
    align-items: center;
    gap: 12px;
    font-weight: 700;
    letter-spacing: -0.5px;
  }
  .wordmark__dot {
    border-radius: 50%;
    background: var(--brand-red);
    flex: none;
  }
  .card--front .wordmark { font-size: 40px; color: var(--on-dark); }
  .card--front .wordmark__dot { width: 48px; height: 48px; }
  .card--back .wordmark {
    position: absolute;
    left: 40px;
    top: 160px;
    font-size: 30px;
    color: var(--ink);
  }
  .card--back .wordmark__dot { width: 36px; height: 36px; }
  .brand-orb {
    position: absolute;
    right: -70px;
    top: -110px;
    width: 330px;
    height: 330px;
    border-radius: 50%;
    background: radial-gradient(circle at 35% 35%, var(--brand-red) 0%, var(--brand-red-deep) 80%);
  }
  .contact {
    position: absolute;
    left: 40px;
    top: 212px;
    color: var(--ink);
    font-size: 11.5px;
    line-height: 1.35;
  }
  .contact__name { color: var(--brand-red); font-weight: 700; font-size: 15px; line-height: 1.2; }
  .contact__role { color: var(--ink-soft); font-size: 11.5px; margin-bottom: 2px; }
  .contact__list { list-style: none; margin-top: 4px; }
  .contact__list li { display: flex; align-items: center; gap: 6px; }
  .contact__icon { width: 11px; height: 11px; flex: none; }
</style>
</head>
<body>
  <section class="card card--front" aria-label="Card front">
    <div class="wordmark"><span class="wordmark__dot"></span><span>DuskVale</span></div>
  </section>

  <section class="card card--back" aria-label="Card back">
    <div class="brand-orb" role="img" aria-label="Large red brand sphere decoration"></div>
    <div class="wordmark"><span class="wordmark__dot"></span><span>DuskVale</span></div>
    <div class="contact">
      <p class="contact__name">Ray Olsen</p>
      <p class="contact__role">Director</p>
      <p>PO Box 4172</p>
      <p>Marlow ACT 2913</p>
      <ul class="contact__list">
        <li>
          <svg class="contact__icon" viewBox="0 0 12 12"><circle cx="6" cy="6" r="5.5" fill="none" stroke="#d4141c"/><path d="M4 3.2l1 1.3-.6.7a4 4 0 0 0 1.9 1.9l.7-.6 1.3 1-.6 1C5.9 8.4 3.6 6.1 3.3 3.8z" fill="#d4141c"/></svg>
          <span>(02) 5550 3186</span>
        </li>
        <li>
          <svg class="contact__icon" viewBox="0 0 12 12"><circle cx="6" cy="6" r="5.5" fill="none" stroke="#d4141c"/><rect x="4.3" y="2.8" width="3.4" height="6.4" rx=".6" fill="none" stroke="#d4141c" stroke-width=".9"/></svg>
          <span>0400 555 217</span>
        </li>
        <li>
          <svg class="contact__icon" viewBox="0 0 12 12"><circle cx="6" cy="6" r="5.5" fill="none" stroke="#d4141c"/><rect x="3" y="4" width="6" height="4.2" fill="none" stroke="#d4141c" stroke-width=".9"/><path d="M3 4l3 2.3L9 4" fill="none" stroke="#d4141c" stroke-width=".9"/></svg>
          <span>ops@duskva.le</span>
        </li>
        <li>
          <svg class="contact__icon" viewBox="0 0 12 12"><circle cx="6" cy="6" r="5.5" fill="none" stroke="#d4141c"/><circle cx="6" cy="6" r="3" fill="none" stroke="#d4141c" stroke-width=".8"/><path d="M3 6h6M6 3c-1.4 1.6-1.4 4.4 0 6M6 3c1.4 1.6 1.4 4.4 0 6" fill="none" stroke="#d4141c" stroke-width=".7"/></svg>
          <span>www.duskva.le</span>
        </li>
      </ul>
    </div>
  </section>
</body>
</html>
```